Brent's Business Cards

My husband is a self employed Cabinet Maker... who contracts to Building companies and clients directly.
He installs kitchesn, designs and also completes renovations and building work.

I would like a small, FUNKY, simple but eye catching design.

It needs to incorporate the following.
Custom Cabinets / Installations / Renovations / Design

Commercial and Residential

He does not have a Website or Facebook,
contact number is 0438 207 964 and email is brentkelway@mailpost.example

I would like a Grey/Silver on black, or blue covering.. I am open to colour designs?

Thank you. :-)

Target Market(s)

Building Companies
Clients
Other Trades people onsite,. to give out at job sites

Industry/Entity Type

Business

Contact Information for Business Card

Phone: 0438 207 964
Email: brentkelway@mailpost.example

Font styles to use
Sans Serif

Colors
0592cd
747474
474747
1b1b1b
85cae6

Requirements
Must have
• Funky, simple, eye catching design
• Would like use of Silver/Grey - and a colour that would complement this.
• Am open to ideas :-)
Nice to have
• We do not have a logo or picture, will leave this up to you if you think an image would be beneficial???
• Thank you.

Files

```html
<!DOCTYPE html>
<html lang="en">
<head>
<meta charset="utf-8">
<title>Brent Kelway – Business Cards</title>
<link rel="stylesheet" href="https://fonts.googleapis.com/css2?family=Michroma&family=Barlow:wght@300;400&display=swap">
<style>
  :root {
    --stage: #2f2c2a;
    --card-black: #151515;
    --ink-white: #ffffff;
    --ink-soft: #e8eaee;
    --accent-blue: #3d74c2;
    --band-blue: #4b86d6;
    --band-light: #85b6ea;
    --band-grey: #6d7888;
    --back-blue-1: #2a62c4;
    --back-blue-2: #0b4ea8;
    --caption: #d8d8d8;
  }
  * { box-sizing: border-box; margin: 0; padding: 0; }
  html, body { width: 1000px; height: 1200px; overflow: hidden; }
  body {
    background: var(--stage);
    position: relative;
    font-family: "Barlow", sans-serif;
  }
  .card {
    position: absolute;
    left: 130px;
    width: 740px;
    height: 457px;
    overflow: hidden;
  }
  .card--front { top: 120px; background: var(--card-black); }
  .card--back  { top: 638px; }

  .card__render {
    position: absolute;
    inset: 0;
    background:
      radial-gradient(ellipse 340px 300px at 600px 130px, #4a4a4c 0%, #2b2b2d 45%, rgba(21,21,21,0) 100%);
  }
  .card__bands { position: absolute; inset: 0; }

  .name {
    font-family: "Michroma", sans-serif;
    font-size: 34px;
    letter-spacing: 1px;
    color: var(--ink-white);
    white-space: nowrap;
  }
  .name__first { color: var(--accent-blue); }
  .services {
    font-weight: 400;
    font-size: 18.5px;
    line-height: 27px;
    letter-spacing: 0.4px;
    color: var(--ink-soft);
  }

  .card--front .name { position: absolute; left: 45px; top: 134px; }
  .card--front .services { position: absolute; left: 45px; top: 182px; }
  .contact {
    position: absolute;
    left: 45px;
    top: 300px;
    list-style: none;
    font-size: 20px;
    font-weight: 300;
    color: var(--ink-white);
    letter-spacing: 0.3px;
  }
  .contact li { display: flex; align-items: center; height: 31px; }
  .contact svg { width: 20px; height: 20px; margin-right: 9px; fill: var(--accent-blue); }

  .card__blueprint {
    position: absolute;
    inset: 0;
    background: linear-gradient(160deg, var(--back-blue-1) 0%, #1a58b8 50%, var(--back-blue-2) 100%);
  }
  .card--back .center {
    position: absolute;
    left: 0; right: 0; top: 178px;
    text-align: center;
  }
  .card--back .name { color: var(--ink-white); font-size: 35px; }
  .card--back .services { margin-top: 8px; }
  .rule {
    width: 124px; height: 7px;
    background: var(--ink-white);
    margin: 20px auto 0;
  }
  .caption {
    position: absolute;
    font-family: "Barlow", sans-serif;
    font-size: 20px;
    color: var(--caption);
  }
  .caption--front { left: 138px; top: 590px; color: #fff; }
  .caption--back  { left: 798px; top: 1115px; }
</style>
</head>
<body>

<section class="card card--front">
  <div class="card__render" role="img" aria-label="Dark 3D render of cabinet frames over architectural plans"></div>
  <svg class="card__bands" viewBox="0 0 740 457" aria-hidden="true">
    <polygon points="740,55 740,110 535,457 500,457" fill="var(--band-grey)" opacity="0.85"/>
    <polygon points="740,110 740,457 545,457" fill="var(--band-blue)" role="img" aria-label="Blue floor plan drawing"/>
    <polygon points="740,115 740,175 585,457 560,457" fill="var(--band-light)"/>
    <polygon points="740,210 740,228 560,457 538,457" fill="var(--ink-white)"/>
  </svg>
  <h1 class="name"><span class="name__first">Brent</span> Kelway</h1>
  <p class="services">Custom Cabinets / Installations / Renovations / Design<br>Commercial and Residential</p>
  <ul class="contact">
    <li>
      <svg viewBox="0 0 24 24"><path d="M6.6 10.8a15.1 15.1 0 0 0 6.6 6.6l2.2-2.2c.3-.3.7-.4 1-.2 1.1.4 2.3.6 3.6.6.6 0 1 .4 1 1V20c0 .6-.4 1-1 1A17 17 0 0 1 3 4c0-.6.4-1 1-1h3.5c.6 0 1 .4 1 1 0 1.3.2 2.5.6 3.6.1.3 0 .7-.2 1z"/></svg>
      0438 207 964
    </li>
    <li>
      <svg viewBox="0 0 24 24"><path d="M2 5h20v14H2z M2 5l10 8 10-8" fill="var(--accent-blue)" stroke="var(--card-black)" stroke-width="1.5"/></svg>
      brentkelway@mailpost.example
    </li>
  </ul>
</section>
<p class="caption caption--front">Front</p>

<section class="card card--back">
  <div class="card__blueprint" role="img" aria-label="Blue-tinted architectural floor plans and cabinet render"></div>
  <div class="center">
    <h2 class="name">Brent Kelway</h2>
    <p class="services">Custom Cabinets / Installations / Renovations / Design<br>Commercial and Residential</p>
    <div class="rule"></div>
  </div>
</section>
<p class="caption caption--back">Back</p>

</body>
</html>
```